Hi Marlow,

I would like you to design for me a menu board for all my products.

The layout I have hand drawn for you so just follow my layout.

Pho
Noodle salads
Rice
StirFry with Thick Rice Noodles
Spring Rolls Ricepaper Rolls

Poster Size: AO Vertical ( 841W x 1189H)

There are more photos of the rice dishes but I thought I can send this through so you can start and I can send you the rest of the photos when I get back from my photographer.

I will have items descriptions to follow also

Requirements
Must have

```html
<!DOCTYPE html>
<html lang="en">
<head>
<meta charset="utf-8">
<title>Menu of the Day</title>
<link rel="stylesheet" href="https://fonts.googleapis.com/css2?family=Ultra&family=Open+Sans:wght@400;600&display=swap">
<style>
  :root {
    --bg-top: #2d5d61;
    --bg-bottom: #0d2123;
    --yellow: #ffe600;
    --white: #ffffff;
    --chef-blue: #2f7fd1;
    --plate-dark: #1b1b1b;
  }
  html, body { margin: 0; padding: 0; overflow: hidden; }
  .board {
    position: relative;
    width: 848px; height: 1200px; overflow: hidden;
    background: radial-gradient(ellipse 90% 60% at 50% 0%, var(--bg-top) 0%, #1a3c3f 55%, var(--bg-bottom) 100%);
    font-family: "Open Sans", Arial, sans-serif;
    color: var(--white);
  }
  .abs { position: absolute; }

  /* star rules */
  .star-rule { position: absolute; border-top: 2px solid var(--white); border-bottom: 2px solid var(--white); padding: 3px 0; }
  .star-rule::before, .star-rule::after { content: ""; display: block; border-top: 2px solid var(--white); }
  .star-rule::before { margin-bottom: 8px; }
  .star-rule::after { margin-top: 8px; }
  .stars { display: flex; justify-content: space-between; padding: 0 6px; height: 20px; }
  .stars svg { width: 20px; height: 20px; fill: var(--yellow); }

  /* title */
  .title { position: absolute; left: 0; width: 848px; text-align: center; font-family: "Ultra", Georgia, serif; color: var(--white); margin: 0; letter-spacing: 2px; }
  .title-main { top: 18px; font-size: 92px; line-height: 1; }
  .title-sub { top: 124px; font-size: 46px; line-height: 1; }

  /* sections */
  .section-name {
    position: absolute; margin: 0;
    font-family: "Ultra", Georgia, serif; color: var(--yellow);
    line-height: 1.02; letter-spacing: 0.5px;
    border-top: 3px solid var(--yellow); border-bottom: 3px solid var(--yellow);
    padding: 3px 0 2px;
  }
  .section-desc { position: absolute; margin: 0; font-size: 10px; line-height: 1.4; color: var(--white); }

  /* dishes */
  .dish { position: absolute; }
  .photo { display: block; border-radius: 14px; width: 100%; }
  .photo-bowl { background: radial-gradient(ellipse 60% 55% at 50% 55%, #f3efe6 0%, #d9b68a 35%, #7a4a2a 62%, var(--plate-dark) 100%); }
  .photo-salad { background: radial-gradient(ellipse 60% 55% at 50% 55%, #c98b4e 0%, #a86a3a 35%, #f0ede6 62%, var(--plate-dark) 100%); }
  .photo-rice { background: radial-gradient(ellipse 65% 60% at 50% 50%, #b98a5a 0%, #d9c3a0 45%, #f2efea 75%, #cfcac3 100%); }
  .photo-noodle { background: radial-gradient(ellipse 65% 60% at 50% 50%, #6b3d1e 0%, #9b6434 45%, #d8d2c6 80%, #a9a39a 100%); }
  .photo-fried { background: radial-gradient(ellipse 60% 55% at 40% 55%, #e0a35a 0%, #b4652c 45%, #4a2c1c 80%, #1d1d1d 100%); }
  .photo-paper { background: linear-gradient(160deg, #2a2a2a 0%, #e9e6df 45%, #c7a074 80%, #8a6240 100%); }
  .tag {
    display: flex; justify-content: flex-end; align-items: center; gap: 4px;
    margin-top: 8px; font-family: "Ultra", Georgia, serif; font-size: 18px; color: var(--yellow); line-height: 1;
  }
  .tag-dot { width: 20px; height: 20px; border-radius: 50%; background: var(--yellow); flex: none; }
  .chef-mark { position: absolute; top: -10px; left: 16px; width: 30px; height: 30px; border-radius: 50%; background: var(--chef-blue); border: 2px solid var(--white); box-sizing: border-box; }

  .chef-badge { position: absolute; left: 666px; top: 948px; }
</style>
</head>
<body>
<div class="board">
  <svg width="0" height="0" style="position:absolute" aria-hidden="true">
    <symbol id="star" viewBox="0 0 20 20"><polygon points="10,1 12.6,7.2 19.3,7.6 14.2,12 15.8,18.6 10,15 4.2,18.6 5.8,12 0.7,7.6 7.4,7.2"/></symbol>
  </svg>

  <!-- header -->
  <div class="star-rule" style="left:18px; top:84px; width:216px;">
    <div class="stars"><svg><use href="#star"/></svg><svg><use href="#star"/></svg><svg><use href="#star"/></svg><svg><use href="#star"/></svg><svg><use href="#star"/></svg><svg><use href="#star"/></svg></div>
  </div>
  <div class="star-rule" style="left:612px; top:84px; width:218px;">
    <div class="stars"><svg><use href="#star"/></svg><svg><use href="#star"/></svg><svg><use href="#star"/></svg><svg><use href="#star"/></svg><svg><use href="#star"/></svg><svg><use href="#star"/></svg></div>
  </div>
  <h1 class="title title-main">MENU</h1>
  <p class="title title-sub">OF THE DAY</p>

  <!-- Pho -->
  <h2 class="section-name" style="left:33px; top:198px; font-size:34px;">PHO</h2>
  <p class="section-desc" style="left:33px; top:254px; width:112px;">Lorem ipsum dolor sit amet, consectetur adipiscing elit. Duis ornare, lectus eu condimentum dictum</p>
  <div class="dish" style="left:154px; top:202px; width:205px;">
    <div class="photo photo-bowl" style="height:174px;" role="img" aria-label="Beef pho in a white bowl with herbs and onion"></div>
    <span class="chef-mark" role="img" aria-label="Chef recommendation mark"></span>
    <div class="tag"><span class="tag-dot" role="img" aria-label="Beef icon"></span>BEEF</div>
  </div>
  <div class="dish" style="left:383px; top:202px; width:206px;">
    <div class="photo photo-bowl" style="height:174px;" role="img" aria-label="Chicken pho in a white bowl with herbs and onion"></div>
    <span class="chef-mark" role="img" aria-label="Chef recommendation mark"></span>
    <div class="tag"><span class="tag-dot" role="img" aria-label="Chicken icon"></span>CHICKEN</div>
  </div>
  <div class="dish" style="left:612px; top:202px; width:206px;">
    <div class="photo photo-fried" style="height:174px;" role="img" aria-label="Tofu pho in a white bowl"></div>
    <div class="tag"><span class="tag-dot" role="img" aria-label="Tofu icon"></span>TOFU</div>
  </div>

  <!-- Noodle salad -->
  <h2 class="section-name" style="left:33px; top:434px; font-size:25px;">NOODLE<br>SALAD</h2>
  <p class="section-desc" style="left:33px; top:499px; width:112px;">Lorem ipsum dolor sit amet, consectetur adipiscing elit. Duis ornare, lectus eu condimentum dictum</p>
  <div class="dish" style="left:160px; top:437px; width:157px;">
    <div class="photo photo-salad" style="height:120px;" role="img" aria-label="Beef noodle salad"></div>
    <span class="chef-mark" role="img" aria-label="Chef recommendation mark"></span>
    <div class="tag"><span class="tag-dot" role="img" aria-label="Beef icon"></span>BEEF</div>
  </div>
  <div class="dish" style="left:326px; top:437px; width:157px;">
    <div class="photo photo-salad" style="height:120px;" role="img" aria-label="Chicken noodle salad"></div>
    <div class="tag"><span class="tag-dot" role="img" aria-label="Chicken icon"></span>CHICKEN</div>
  </div>
  <div class="dish" style="left:492px; top:437px; width:157px;">
    <div class="photo photo-salad" style="height:120px;" role="img" aria-label="BBQ pork noodle salad"></div>
    <span class="chef-mark" role="img" aria-label="Chef recommendation mark"></span>
    <div class="tag"><span class="tag-dot" role="img" aria-label="Pork icon"></span>BBQ PORK</div>
  </div>
  <div class="dish" style="left:658px; top:437px; width:157px;">
    <div class="photo photo-salad" style="height:120px;" role="img" aria-label="Tofu noodle salad"></div>
    <span class="chef-mark" role="img" aria-label="Chef recommendation mark"></span>
    <div class="tag"><span class="tag-dot" role="img" aria-label="Tofu icon"></span>TOFU</div>
  </div>

  <!-- Rice -->
  <h2 class="section-name" style="left:33px; top:619px; font-size:30px;">RICE</h2>
  <p class="section-desc" style="left:33px; top:669px; width:112px;">Lorem ipsum dolor sit amet, consectetur adipiscing elit. Duis ornare, lectus eu condimentum dictum</p>
  <div class="dish" style="left:160px; top:620px; width:157px;">
    <div class="photo photo-rice" style="height:120px;" role="img" aria-label="Beef rice dish"></div>
    <div class="tag"><span class="tag-dot" role="img" aria-label="Beef icon"></span>BEEF</div>
  </div>
  <div class="dish" style="left:326px; top:620px; width:157px;">
    <div class="photo photo-rice" style="height:120px;" role="img" aria-label="Chicken rice dish"></div>
    <div class="tag"><span class="tag-dot" role="img" aria-label="Chicken icon"></span>CHICKEN</div>
  </div>
  <div class="dish" style="left:492px; top:620px; width:157px;">
    <div class="photo photo-rice" style="height:120px;" role="img" aria-label="Tofu rice dish"></div>
    <div class="tag"><span class="tag-dot" role="img" aria-label="Tofu icon"></span>TOFU</div>
  </div>
  <div class="dish" style="left:658px; top:620px; width:157px;">
    <div class="photo photo-rice" style="height:120px;" role="img" aria-label="Fried rice with prawns"></div>
    <span class="chef-mark" role="img" aria-label="Chef recommendation mark"></span>
    <div class="tag"><span class="tag-dot" role="img" aria-label="Fried rice icon"></span>FRIED RICE</div>
  </div>

  <!-- Stir fry -->
  <h2 class="section-name" style="left:33px; top:801px; font-size:22px; width:230px;">STIRFRY W THICK<br>RICE NOODLE</h2>
  <p class="section-desc" style="left:33px; top:869px; width:225px;">Lorem ipsum dolor sit amet, consectetur adipiscing elit. Duis ornare, lectus eu condimentum dictum</p>
  <div class="dish" style="left:324px; top:801px; width:157px;">
    <div class="photo photo-noodle" style="height:120px;" role="img" aria-label="Beef stir fry with thick rice noodles"></div>
    <div class="tag"><span class="tag-dot" role="img" aria-label="Beef icon"></span>BEEF</div>
  </div>
  <div class="dish" style="left:490px; top:801px; width:157px;">
    <div class="photo photo-noodle" style="height:120px;" role="img" aria-label="Chicken stir fry with thick rice noodles"></div>
    <div class="tag"><span class="tag-dot" role="img" aria-label="Chicken icon"></span>CHICKEN</div>
  </div>
  <div class="dish" style="left:656px; top:801px; width:157px;">
    <div class="photo photo-noodle" style="height:120px;" role="img" aria-label="Tofu stir fry with thick rice noodles"></div>
    <div class="tag"><span class="tag-dot" role="img" aria-label="Tofu icon"></span>TOFU</div>
  </div>

  <!-- Rolls -->
  <h2 class="section-name" style="left:33px; top:979px; font-size:22px;">SPRING<br>ROLLS</h2>
  <p class="section-desc" style="left:33px; top:1037px; width:112px;">Lorem ipsum dolor sit amet, consectetur adipiscing elit. Duis ornare, lectus eu condimentum dictum</p>
  <div class="dish" style="left:160px; top:981px; width:157px;">
    <div class="photo photo-fried" style="height:120px;" role="img" aria-label="Fried spring rolls with chilli dipping sauce"></div>
  </div>
  <h2 class="section-name" style="left:339px; top:979px; font-size:22px; width:134px;">RICEPAPER<br>ROLLS</h2>
  <p class="section-desc" style="left:339px; top:1037px; width:112px;">Lorem ipsum dolor sit amet, consectetur adipiscing elit. Duis ornare, lectus eu condimentum dictum</p>
  <div class="dish" style="left:492px; top:981px; width:157px;">
    <div class="photo photo-paper" style="height:120px;" role="img" aria-label="Fresh ricepaper rolls on a wooden board"></div>
    <span class="chef-mark" role="img" aria-label="Chef recommendation mark"></span>
  </div>

  <svg class="chef-badge" width="150" height="150" viewBox="0 0 150 150" role="img" aria-label="Chef recommendation badge">
    <defs><path id="badge-arc" d="M 22 80 A 53 53 0 1 1 128 80"/></defs>
    <text font-family="Open Sans, Arial, sans-serif" font-weight="600" font-size="12" fill="#ffffff" letter-spacing="0.5">
      <textPath href="#badge-arc" startOffset="50%" text-anchor="middle">CHEF RECOMMENDATION</textPath>
    </text>
    <circle cx="75" cy="85" r="45" fill="#ffffff"/>
    <circle cx="75" cy="85" r="39" fill="var(--chef-blue)"/>
  </svg>

  <!-- footer -->
  <div class="star-rule" style="left:18px; top:1125px; width:812px;">
    <div class="stars"><svg><use href="#star"/></svg><svg><use href="#star"/></svg><svg><use href="#star"/></svg><svg><use href="#star"/></svg><svg><use href="#star"/></svg><svg><use href="#star"/></svg><svg><use href="#star"/></svg><svg><use href="#star"/></svg><svg><use href="#star"/></svg><svg><use href="#star"/></svg><svg><use href="#star"/></svg><svg><use href="#star"/></svg><svg><use href="#star"/></svg><svg><use href="#star"/></svg><svg><use href="#star"/></svg><svg><use href="#star"/></svg><svg><use href="#star"/></svg><svg><use href="#star"/></svg><svg><use href="#star"/></svg><svg><use href="#star"/></svg><svg><use href="#star"/></svg><svg><use href="#star"/></svg></div>
  </div>
</div>
</body>
</html>
```